Infill Flyer

We would like a flyer designed.

8.5 inches x 11 inches

Clean, fresh, professional, scientific look

I realize that a few of my photos are not high resolution, but I will be using this for electronic transmission for now. Thanks!

Industry/Entity Type

Electronic

Font styles to use
Sans Serif

```html
<!DOCTYPE html>
<html lang="en">
<head>
<meta charset="utf-8">
<title>Infill Options Flyer</title>
<link href="https://fonts.googleapis.com/css2?family=Open+Sans:wght@400;600&display=swap" rel="stylesheet">
<style>
  :root {
    --orange: #e87722;
    --orange-soft: #fbe3cf;
    --text: #3a3a3a;
    --muted: #8a8a8a;
    --paper: #ffffff;
  }
  * { margin: 0; padding: 0; box-sizing: border-box; }
  html, body { width: 925px; height: 1200px; overflow: hidden; background: var(--paper); }
  body { font-family: "Open Sans", Arial, sans-serif; color: var(--text); }
  .flyer { position: relative; width: 925px; height: 1200px; padding: 70px 46px 0 46px; }
  .flyer-title { color: var(--orange); font-weight: 400; font-size: 26px; line-height: 1.2; margin-bottom: 10px; }
  .intro { color: var(--muted); font-size: 15px; line-height: 21px; max-width: 420px; margin-bottom: 28px; }
  .option { margin-bottom: 22px; }
  .option-header {
    display: flex; align-items: stretch; height: 56px;
    border-top: 2px solid var(--orange);
    margin-bottom: 16px;
  }
  .option-header.tall { height: 88px; }
  .option-label {
    width: 360px; display: flex; align-items: center; padding-left: 10px;
    font-size: 23px; color: var(--orange); font-weight: 400;
    background: linear-gradient(180deg, var(--orange-soft) 0%, var(--paper) 100%);
  }
  .option-media { flex: 1; }
  .media-grind { background: linear-gradient(90deg, #2a2a2a, #4a4a4a 30%, #2f2f35 60%, #3c3c3c); }
  .media-tpe { background: linear-gradient(135deg, #d8c5a0, #c9b07e 40%, #e2d2b0 70%, #bfa370); }
  .media-epdm { background: linear-gradient(90deg, #f4f4f0 0%, #9bb06a 30%, #6d8a3e 60%, #86a052); }
  .option-body { font-size: 15px; line-height: 21px; color: var(--text); padding-right: 20px; }
</style>
</head>
<body>
<main class="flyer">
  <h1 class="flyer-title">Are there other infill options?</h1>
  <p class="intro">Yes. There are many other infill options. However, there are drawbacks to everything. And, frankly, nothing has been tested to the extent that crumb rubber has, especially for the price. As a point of comparison SBR sells for around $0.20 per pound. A few other infill options include:</p>

  <section class="option">
    <div class="option-header">
      <h2 class="option-label">Stride Grind</h2>
      <div class="option-media media-grind" role="img" aria-label="Close-up of multicoloured ground shoe-rubber granules"></div>
    </div>
    <p class="option-body">Of the all of the non-crumb rubber infill options, this is the most attractive. Stride Grind is exclusively available to FieldCraft customers. It is gathered from the waste of Stride's manufacturing process. While Stride Grind adheres to Stride's stringent environmental and quality standards, nevertheless it has not been subjected the same degree of scrutiny that crumb rubber has undergone. Cost estimate: $0.56 per pound.</p>
  </section>

  <section class="option">
    <div class="option-header tall">
      <h2 class="option-label">TPE</h2>
      <div class="option-media media-tpe" role="img" aria-label="Close-up of beige thermoplastic elastomer pellets"></div>
    </div>
    <p class="option-body">TPE—Thermoplastic Elastomer is a polyolefin infill option. Much (but not all) of the TPE around the world comes from China. One problem associated with TPE is the varying quality from ahodgepodge of suppliers. A particularly worrying trend we have seen in the industry is the low melting point of some TPE formulas,which have caused field failures. Additionally, there have been few if any studies on the human health effects of TPE, and FieldCraft has no information about the dyes used in this infill.<br>Cost estimate: $1.24 per pound.</p>
  </section>

  <section class="option">
    <div class="option-header">
      <h2 class="option-label">EPDM</h2>
      <div class="option-media media-epdm" role="img" aria-label="Close-up of green EPDM rubber granules"></div>
    </div>
    <p class="option-body">TPE—Thermoplastic Elastomer is a polyolefin infill option. Much (but not all) of the TPE around the world comes from China. One problem associated with TPE<br>is the varying quality from ahodgepodge of suppliers. A particularly worrying trend<br>we have seen in the industry is the low melting point of some TPE formulas,which have caused field failures. Additionally, there have been few if any studies on the human health effects of TPE, and FieldCraft has no information about the dyes used in this infill.<br>Cost estimate: $1.24 per pound.</p>
  </section>
</main>
</body>
</html>
```